Hadley & Partners, LLC Business Card 2016

We need a new business card design for a very important trade show coming up.

We are a compliance Consulting Firm. Our clients are stock brokerage firms and investment advisers.

I would like our logo on both sides of the card.

Info in the front of the card shold include:

Logo
First & Last Name
Title
Office #
Cell #
Email
Company Address (42 W. Calloway St., Suite 300 Pasadena, CA 91417

Back of the card should include the logo and url: www.hadleypartnersgroup.com

Target Market(s)

Stock Brokerage Firms and Investment Advisers

Industry/Entity Type

Financial Service

Contact Information for Business Card

Marcus J. Pellew
President
42 W. Calloway St., Suite 300
Pasadena, CA 91417
O 626.555.0147 ext. 204
C 818.555.0193
Email: marcus@hadleypartnersgroup.com
www.hadleypartnersgroup.com

Requirements
Nice to have
• The back of the card could be black with the logo with the white letters.
• I do want the front of the card to at least have the color logo with the black "Hadley & Partners Lettering.

```html
<!DOCTYPE html>
<html lang="en">
<head>
<meta charset="utf-8">
<title>Hadley &amp; Partners — Business Card</title>
<link href="https://fonts.googleapis.com/css2?family=Roboto:wght@400;500&family=Saira+Condensed:wght@600&display=swap" rel="stylesheet">
<style>
  :root {
    --stage: #1d1d1d;
    --card-black: #222222;
    --card-white: #ebebeb;
    --red: #b3150f;
    --red-deep: #7a0a06;
    --grey: #6a7077;
    --ink: #1a1a1a;
    --white: #ffffff;
  }
  * { box-sizing: border-box; margin: 0; padding: 0; }
  html, body {
    width: 1200px; height: 1158px; overflow: hidden;
    background: var(--stage);
    font-family: "Roboto", Arial, sans-serif;
  }
  .card {
    position: absolute; left: 248px;
    width: 736px; height: 436px;
    overflow: hidden;
  }
  .card--back { top: 76px; background: var(--card-black); }
  .card--front { top: 608px; background: var(--card-white); }

  .brand {
    position: absolute;
    display: flex; align-items: center; gap: 18px;
    font-family: "Roboto", Arial, sans-serif;
    font-weight: 500;
    white-space: nowrap;
  }
  .brand__mark { width: 64px; height: 64px; background: var(--red); flex: none; }
  .card--back .brand { left: 94px; top: 180px; color: var(--white); font-size: 52px; }
  .card--back .brand__mark { width: 76px; height: 76px; }
  .card--front .brand { left: 20px; top: 150px; color: var(--ink); font-size: 44px; }

  .header-band {
    position: absolute; left: 0; top: 0; width: 736px; height: 128px;
    background: linear-gradient(90deg, var(--grey) 0%, var(--red) 55%, var(--red-deep) 100%);
  }

  .holder {
    position: absolute; right: 39px; top: 30px; text-align: right; color: var(--white);
  }
  .holder__name {
    font-family: "Saira Condensed", "Arial Narrow", sans-serif;
    font-weight: 600; font-size: 31px; line-height: 1.1;
  }
  .holder__title { font-size: 17px; line-height: 1.4; }

  .contacts {
    position: absolute; left: 38px; top: 294px; list-style: none;
    color: var(--ink); font-size: 19px;
  }
  .contacts li { display: flex; align-items: center; height: 26.5px; }
  .contacts svg { width: 18px; height: 18px; margin-right: 19px; fill: var(--red); }

  .address {
    position: absolute; right: 39px; top: 315px; text-align: right;
    font-style: normal; color: var(--ink); font-size: 19px; line-height: 26.5px;
  }
</style>
</head>
<body>

<section class="card card--back">
  <div class="brand"><span class="brand__mark"></span>Hadley &amp; Partners</div>
</section>

<section class="card card--front">
  <div class="header-band" role="img" aria-label="Decorative red and grey header band"></div>

  <div class="holder">
    <div class="holder__name">Marcus J. Pellew</div>
    <div class="holder__title">President</div>
  </div>

  <div class="brand"><span class="brand__mark"></span>Hadley &amp; Partners</div>

  <ul class="contacts">
    <li><svg viewBox="0 0 24 24" aria-hidden="true"><path d="M3 9c0-3 4-5 9-5s9 2 9 5v2h-5V8.5c-2-.6-6-.6-8 0V11H3zM6 12h12l2 8H4z"/></svg>626.555.0147 ext. 204</li>
    <li><svg viewBox="0 0 24 24" aria-hidden="true"><path d="M12 2a10 10 0 1 0 0 20 10 10 0 0 0 0-20zm0 2c1 1.5 1.7 3.5 1.9 6h-3.8c.2-2.5.9-4.5 1.9-6zm-2 .3C9.2 6 8.2 8 8.1 10H4.2A8 8 0 0 1 10 4.3zm4 0A8 8 0 0 1 19.8 10h-3.9c-.1-2-1.1-4-1.9-5.7zM4.2 12h3.9c.1 2 1.1 4 1.9 5.7A8 8 0 0 1 4.2 12zm5.9 0h3.8c-.2 2.5-.9 4.5-1.9 6-1-1.5-1.7-3.5-1.9-6zm5.8 0h3.9a8 8 0 0 1-5.8 5.7c.8-1.7 1.8-3.7 1.9-5.7z"/></svg>818.555.0193</li>
    <li><svg viewBox="0 0 24 24" aria-hidden="true"><path d="M2 5h20v14H2zm2 2v.5l8 6 8-6V7zm0 3v7h16v-7l-8 6z"/></svg>marcus@hadleypartnersgroup.com</li>
    <li><svg viewBox="0 0 24 24" aria-hidden="true"><path d="M12 2a10 10 0 1 0 0 20 10 10 0 0 0 0-20zm0 2c1 1.5 1.7 3.5 1.9 6h-3.8c.2-2.5.9-4.5 1.9-6zm-2 .3C9.2 6 8.2 8 8.1 10H4.2A8 8 0 0 1 10 4.3zm4 0A8 8 0 0 1 19.8 10h-3.9c-.1-2-1.1-4-1.9-5.7zM4.2 12h3.9c.1 2 1.1 4 1.9 5.7A8 8 0 0 1 4.2 12zm5.9 0h3.8c-.2 2.5-.9 4.5-1.9 6-1-1.5-1.7-3.5-1.9-6zm5.8 0h3.9a8 8 0 0 1-5.8 5.7c.8-1.7 1.8-3.7 1.9-5.7z"/></svg>hadleypartnersgroup.com</li>
  </ul>

  <address class="address">
    42 W. Calloway St.,<br>
    Suite 300<br>
    Pasadena, CA 91417
  </address>
</section>

</body>
</html>
```